Lumo4Kart - a fintech company - business card

We need a business card design for our Payments Technology company in Sydney, Australia. We provide business with payment solutions expanding across EFTPOS machines, online payment gateways and mobile payment solutions. We would like to see designs that are clean, classy and professional.
Target Market(s)
Business professionals, executives, c-suite
Industry/Entity Type
Fintech
Contact Information for Business Card
Will be on 400gsm. Logo will most likely be spot gloss unless designer recommends otherwise.
Font styles to use
Sans Serif
Requirements
Must have
- We need our website (lumo4kart.com.au), email (contact@lumo4kart.com.au), mobile (0432 587 904) and direct phone number (02 6815 3927) to feature on the card along with our logo (attached) and the words "EFTPOS | ONLINE | MOBILE"
- Font = Roboto

```html
<!DOCTYPE html>
<html lang="en">
<head>
<meta charset="utf-8">
<title>Lumo4Kart business card</title>
<link rel="stylesheet" href="https://fonts.googleapis.com/css2?family=Roboto:wght@300;400;500;700&family=Open+Sans:wght@400&display=swap">
<style>
  :root {
    --brand-blue: #166092;
    --brand-grey: #616265;
    --swoosh-grey: #6d6e71;
    --paper: #ffffff;
    --backdrop: #3b3c3f;
  }
  * { margin: 0; padding: 0; box-sizing: border-box; }
  html, body {
    width: 1200px; height: 1039px; overflow: hidden;
    background: var(--backdrop);
  }
  .card {
    position: absolute;
    overflow: hidden;
    border-radius: 34px;
  }
  /* Card front */
  .card-front {
    left: 213px; top: 77px; width: 750px; height: 426px;
    background: var(--brand-blue);
  }
  .front-name {
    position: absolute; left: 0; right: 0; top: 160px;
    text-align: center;
    font-family: "Roboto", sans-serif; font-weight: 700;
    font-size: 84px; line-height: 1;
    color: var(--paper);
    text-transform: uppercase;
  }
  .front-url {
    position: absolute; left: 0; right: 0; top: 374px;
    text-align: center;
    font-family: "Open Sans", sans-serif; font-size: 22px;
    letter-spacing: 5px; color: var(--paper);
  }
  /* Card back */
  .card-back {
    left: 205px; top: 530px; width: 773px; height: 441px;
    background: var(--paper);
  }
  .card-back .waves {
    position: absolute; left: 0; top: 0; width: 773px; height: 441px;
  }
  .brand-dot {
    position: absolute; left: 118px; top: 30px;
    width: 112px; height: 112px; border-radius: 50%;
    background: var(--brand-blue);
  }
  .brand-name {
    position: absolute; left: 50px; top: 184px;
    font-family: "Roboto", sans-serif; font-weight: 700;
    font-size: 58px; line-height: 1; letter-spacing: -1px;
    color: var(--brand-grey);
    text-transform: uppercase;
  }
  .tagline {
    position: absolute; left: 51px; top: 247px;
    font-family: "Roboto", sans-serif; font-weight: 300;
    font-size: 24px; line-height: 1;
    color: var(--brand-blue);
  }
  .person {
    position: absolute; left: 465px; top: 48px;
    font-family: "Roboto", sans-serif; line-height: 1;
  }
  .person-name {
    font-weight: 700; font-size: 27px; color: var(--brand-blue);
    text-transform: uppercase;
  }
  .person-title {
    margin-top: 6px;
    font-weight: 500; font-size: 23px; color: var(--brand-grey);
    text-transform: uppercase;
  }
  .contacts {
    position: absolute; right: 30px; top: 291px;
    list-style: none;
    font-family: "Open Sans", sans-serif; font-size: 19px;
    color: var(--paper);
  }
  .contacts li {
    display: flex; align-items: center; justify-content: flex-end;
    height: 30.5px;
  }
  .contacts svg { width: 21px; height: 21px; margin-left: 11px; flex: none; }
</style>
</head>
<body>
  <section class="card card-front">
    <div class="front-name">Lumo4Kart</div>
    <div class="front-url">www.lumo4kart.com.au</div>
  </section>

  <section class="card card-back">
    <svg class="waves" viewBox="0 0 902 514" preserveAspectRatio="none" aria-hidden="true">
      <path fill="var(--swoosh-grey)" d="M0,377 C150,450 420,462 633,285 C440,438 180,458 0,417 Z"/>
      <path fill="var(--brand-blue)" d="M902,25 C780,190 620,385 330,440 C200,464 80,456 0,442 L0,514 L902,514 Z"/>
    </svg>

    <div class="brand-dot"></div>
    <div class="brand-name">Lumo4Kart</div>
    <div class="tagline">EFTPOS | ONLINE | MOBILE</div>

    <div class="person">
      <div class="person-name">Maren Holloway</div>
      <div class="person-title">President</div>
    </div>

    <ul class="contacts">
      <li>0432 587 904
        <svg viewBox="0 0 24 24"><path fill="#fff" d="M6.6 2.5l3 3.2c.5.5.5 1.2.1 1.7L8.2 9.1c1.3 2.7 3.6 5 6.3 6.4l1.7-1.6c.5-.4 1.2-.4 1.7.1l3.1 3c.5.5.5 1.2 0 1.7l-1.7 1.8c-.6.6-1.5.8-2.3.5C10.4 19 5 13.6 3 7c-.2-.8 0-1.7.6-2.3l1.6-1.9c.4-.5 1-.5 1.4-.3z"/></svg>
      </li>
      <li>02 6815 3927
        <svg viewBox="0 0 24 24"><circle cx="12" cy="12" r="10.5" fill="none" stroke="#fff" stroke-width="1.6"/><rect x="8.5" y="6" width="7" height="12" rx="1.2" fill="none" stroke="#fff" stroke-width="1.6"/><line x1="10.5" y1="15.6" x2="13.5" y2="15.6" stroke="#fff" stroke-width="1.4"/></svg>
      </li>
      <li>contact@lumo4kart.com.au
        <svg viewBox="0 0 24 24"><rect x="2" y="5" width="20" height="14" fill="#fff"/><path d="M2.5 5.5L12 13l9.5-7.5M2.5 18.5l7-6.5M21.5 18.5l-7-6.5" fill="none" stroke="var(--brand-blue)" stroke-width="1.6"/></svg>
      </li>
      <li>www.lumo4kart.com.au
        <svg viewBox="0 0 24 24"><g fill="none" stroke="#fff" stroke-width="1.5"><circle cx="12" cy="12" r="10"/><ellipse cx="12" cy="12" rx="4.5" ry="10"/><line x1="2" y1="12" x2="22" y2="12"/><path d="M4 6.5h16M4 17.5h16"/></g></svg>
      </li>
    </ul>
  </section>
</body>
</html>
```